Upmarket Bathroom and Kitchen ware supplier needs a classy business card design

We are a company based in Fiji, we sell plumbing ware (Kitchen and bathroom taps, Basins,showers, toilets etc) through up market show rooms to individuals and directly through Architects and designers of resorts and holiday houses for new builds and renovations. we are wanting to upgrade our over all look and brand. we are starting with a new logo but will be rebranding the whole business. This project is for a business card design for my management and tales team I would like it to be dark, classy and interesting

Target Market(s)

Resort directors and Management, High end holiday home owners

Contact Information for Business Card

Neil Dawson
Director
+64219473815

Colors

Designer to choose colors to be used in the design.

Requirements
Must have
• Must have an upmarket appearance I like darker charcoal shades but will be guided by the designers
• Please any catch phrases like "Crafting remarkable living rooms" this belongs tpo one of our suppliers so can not be used.
Nice to have
• Double sided, so front dedicated to logo provided and back info about the business and the person.

```html
<!DOCTYPE html>
<html lang="en">
<head>
<meta charset="utf-8">
<title>Halcyon Interiors – Business Card</title>
<link href="https://fonts.googleapis.com/css2?family=Lato:wght@300;400;700&display=swap" rel="stylesheet">
<style>
  :root {
    --backdrop: #1d1d1d;
    --card: #272727;
    --accent: #b3232a;
    --ink: #f2f2f2;
    --muted: #cfcfcf;
    --rule: #8a8a8a;
  }
  * { margin: 0; padding: 0; box-sizing: border-box; }
  html, body {
    width: 1200px; height: 1200px; overflow: hidden;
    background: var(--backdrop);
    font-family: "Lato", Arial, sans-serif;
  }
  .sheet {
    width: 1200px; height: 1200px;
    display: flex; flex-direction: column; align-items: center; justify-content: center;
    gap: 60px;
  }
  .card {
    position: relative;
    width: 875px; height: 500px;
    background: var(--card);
    border-bottom: 6px solid var(--accent);
    box-shadow: 0 18px 40px rgba(0,0,0,0.45);
  }
  .wordmark {
    display: flex; align-items: center; gap: 18px;
  }
  .wordmark__dot {
    border-radius: 50%; background: var(--accent); flex: none;
  }
  .wordmark__name {
    font-weight: 300; color: var(--ink);
    text-transform: uppercase; white-space: nowrap;
  }

  /* Back: identity + contact */
  .card--back .wordmark {
    position: absolute; left: 70px; top: 50%; transform: translateY(-50%);
  }
  .card--back .wordmark__dot { width: 34px; height: 34px; }
  .card--back .wordmark__name { font-size: 20px; letter-spacing: 5px; }
  .divider {
    position: absolute; left: 468px; top: 120px;
    width: 2px; height: 260px; background: var(--accent);
  }
  .contact {
    position: absolute; left: 510px; top: 138px;
  }
  .contact__name {
    color: var(--accent); font-weight: 700; font-size: 30px;
    text-transform: uppercase; letter-spacing: 1px;
  }
  .contact__role {
    color: var(--muted); font-size: 18px; font-weight: 400;
    margin: 8px 0 26px;
  }
  .contact__list { list-style: none; }
  .contact__item {
    display: flex; align-items: center; gap: 14px;
    color: var(--ink); font-size: 19px; font-weight: 400;
    margin-bottom: 12px;
  }
  .contact__icon { width: 18px; height: 18px; flex: none; }

  /* Front: centred identity */
  .card--front .wordmark {
    position: absolute; left: 50%; top: 50%; transform: translate(-50%, -50%);
    gap: 28px;
  }
  .card--front .wordmark__dot { width: 64px; height: 64px; }
  .card--front .wordmark__name { font-size: 34px; letter-spacing: 9px; }
</style>
</head>
<body>
<main class="sheet">

  <section class="card card--back" aria-label="Card back">
    <div class="wordmark">
      <span class="wordmark__dot"></span>
      <span class="wordmark__name">Halcyon Interiors</span>
    </div>
    <div class="divider"></div>
    <div class="contact">
      <h1 class="contact__name">Marcus Hale</h1>
      <p class="contact__role">President</p>
      <ul class="contact__list">
        <li class="contact__item">
          <svg class="contact__icon" viewBox="0 0 24 24" aria-hidden="true"><path fill="#b3232a" d="M6.6 10.8a15.1 15.1 0 0 0 6.6 6.6l2.2-2.2a1 1 0 0 1 1-.25 11.4 11.4 0 0 0 3.6.57 1 1 0 0 1 1 1V20a1 1 0 0 1-1 1A17 17 0 0 1 3 4a1 1 0 0 1 1-1h3.5a1 1 0 0 1 1 1c0 1.25.2 2.45.57 3.57a1 1 0 0 1-.25 1z"/></svg>
          +679 331 4820
        </li>
        <li class="contact__item">
          <svg class="contact__icon" viewBox="0 0 24 24" aria-hidden="true"><rect x="2.5" y="5" width="19" height="14" fill="none" stroke="#b3232a" stroke-width="2"/><path d="M3 6l9 7 9-7" fill="none" stroke="#b3232a" stroke-width="2"/></svg>
          info@halcyonbath.com
        </li>
        <li class="contact__item">
          <svg class="contact__icon" viewBox="0 0 24 24" aria-hidden="true"><circle cx="12" cy="12" r="9.5" fill="none" stroke="#b3232a" stroke-width="2"/><ellipse cx="12" cy="12" rx="4" ry="9.5" fill="none" stroke="#b3232a" stroke-width="1.6"/><path d="M2.5 12h19" stroke="#b3232a" stroke-width="1.6"/></svg>
          www.halcyonbath.com
        </li>
      </ul>
    </div>
  </section>

  <section class="card card--front" aria-label="Card front">
    <div class="wordmark">
      <span class="wordmark__dot"></span>
      <span class="wordmark__name">Halcyon Interiors</span>
    </div>
  </section>

</main>
</body>
</html>
```